We need a MODERN credit application banner

We have a program that helps people get pre-qualified for an auto loan. Our current Application page/Success page is dated and does not have the colors we want. I want to use fonts and colors that match our partner CrestLedger (www.crestledger-demo.com). I want to include their powered by logo, tallymark rating logo, and swift4lending logo all in a matching CrestLedger Color scheme. I also need a Favicon that matches your design for the page. I attached our deck so you can get more content. To be clear the application page and success pages below are the targets of this redesign! You can visit www.pbelvoiradvertising-demo.com to get more information from our website or www.swift4lending-demo.com.

Target Market(s)

Car dealers and their consumers

Industry/Entity Type

Automotive

Requirements
Must have
• It must offer the same data that is on the existing art
Nice to have
• Looking for a Clean but Interesting design.
Should not have
• No red and black. Do not change the form fills.

```html
<!DOCTYPE html>
<html lang="en">
<head>
<meta charset="UTF-8">
<title>Free Credit Score – Pre-Qualify Banner</title>
<link rel="stylesheet" href="https://fonts.googleapis.com/css2?family=Montserrat:wght@600;700;800&family=Open+Sans:wght@300;400;700&display=swap">
<style>
  :root{
    --teal-deep:#0a5466;
    --teal-panel:#0c6579;
    --yellow:#fcd800;
    --ink:#0c5a6e;
    --field:#ffffff;
    --field-text:#3d3d3d;
    --white:#ffffff;
  }
  *{box-sizing:border-box;margin:0;padding:0}
  html,body{width:1200px;height:603px;overflow:hidden;background:var(--teal-deep)}
  .banner{position:relative;width:1200px;height:603px;background:var(--teal-deep);font-family:"Open Sans",Arial,sans-serif}
  .hero-photo{position:absolute;left:441px;top:0;width:759px;height:430px;
    background:linear-gradient(115deg,#cfd4d6 0%,#8f979b 22%,#5b6468 40%,#3a7a3e 58%,#5d8c44 70%,#b9bec0 88%,#e4e6e7 100%)}
  .headline{position:absolute;left:33px;top:33px;color:var(--white);font-family:"Montserrat",Arial,sans-serif}
  .headline h1{font-size:23px;font-weight:700;letter-spacing:.4px;line-height:28px}
  .headline p{font-size:15.5px;font-weight:700;margin-top:7px;margin-left:2px}
  .form-panel{position:absolute;left:41px;top:126px;width:615px;height:437px;background:var(--teal-panel)}
  .field{position:absolute;width:266px;height:40px;background:var(--field);color:var(--field-text);
    font-size:12.5px;font-weight:300;display:flex;align-items:center;padding-left:16px}
  .col-a{left:38px}.col-b{left:320px}
  .dob{display:flex;padding:0;background:transparent}
  .dob span{background:var(--field);height:40px;display:flex;align-items:center;margin-right:1px}
  .dob .dob-label{width:108px;padding-left:15px}
  .dob .dd{width:49px;padding-left:9px}
  .dob .mm{width:48px;padding-left:8px}
  .dob .yy{width:57px;padding-left:8px;margin-right:0}
  .caret{display:inline-block;width:0;height:0;border-left:4px solid transparent;border-right:4px solid transparent;border-top:5px solid #333;margin-left:5px}
  .select .caret{position:absolute;right:16px;top:18px;border-left-width:5px;border-right-width:5px;border-top-width:6px}
  .vehicle-label{position:absolute;left:37px;top:290px;color:var(--white);font-size:12.5px;font-weight:700}
  .cta{position:absolute;left:37px;top:372px;width:552px;height:46px;background:var(--yellow);color:var(--ink);
    font-family:"Montserrat",Arial,sans-serif;font-weight:700;font-size:16px;display:flex;align-items:center;justify-content:center;letter-spacing:.3px}
  .benefit{position:absolute;top:389px;width:154px;height:174px;background:var(--yellow);color:var(--ink);
    font-family:"Montserrat",Arial,sans-serif;font-weight:700;text-align:center}
  .benefit svg{position:absolute;left:50%;transform:translateX(-50%)}
  .benefit h2{position:absolute;left:0;right:0;font-size:15px;line-height:26px;font-weight:700}
  .powered{position:absolute;left:0;right:0;top:126px;line-height:17px}
  .powered small{display:block;font-size:11px;font-weight:600}
  .powered strong{font-size:15px;font-weight:700}
</style>
</head>
<body>
<div class="banner">
  <div class="hero-photo" role="img" aria-label="Photo of a smiling driver giving a thumbs up from a car window"></div>

  <div class="headline">
    <h1>GET YOUR FREE CREDIT SCORE</h1>
    <p>And Get Pre-Qualifies Instantly</p>
  </div>

  <div class="form-panel">
    <div class="field col-a" style="top:24px">First Name *</div>
    <div class="field col-b" style="top:24px">Last Name *</div>
    <div class="field col-a" style="top:76px">Address *</div>
    <div class="field col-b" style="top:76px">Apartment</div>
    <div class="field col-a" style="top:128px">City *</div>
    <div class="field col-b" style="top:128px">State*</div>
    <div class="field col-a" style="top:180px">Zip *</div>
    <div class="field col-b dob" style="top:180px">
      <span class="dob-label">Date of Birth</span>
      <span class="dd">DD<i class="caret"></i></span>
      <span class="mm">MM<i class="caret"></i></span>
      <span class="yy">YYYY<i class="caret"></i></span>
    </div>
    <div class="field col-a" style="top:232px">Mobile Phone *</div>
    <div class="field col-b" style="top:232px">Email*</div>
    <div class="vehicle-label">The Vehile I’m Interested in is</div>
    <div class="field col-a select" style="top:315px">Category<i class="caret"></i></div>
    <div class="field col-b select" style="top:315px">Make<i class="caret"></i></div>
    <div class="cta">GET RESULTS</div>
  </div>

  <div class="benefit" style="left:682px">
    <svg width="48" height="34" viewBox="0 0 48 34" style="top:24px" fill="none" stroke="#0c5a6e" stroke-width="3">
      <path d="M4 30 A20 20 0 0 1 44 30 Z" stroke-linejoin="round"/>
      <path d="M10 30 A14 14 0 0 1 38 30"/>
      <line x1="24" y1="30" x2="31" y2="18"/>
      <circle cx="24" cy="29" r="3" fill="#0c5a6e"/>
    </svg>
    <h2 style="top:68px;line-height:21px">Free Credit<br>Score</h2>
    <div class="powered"><small>Powered by</small><strong>CrestLedger</strong></div>
  </div>

  <div class="benefit" style="left:850px">
    <svg width="50" height="50" viewBox="0 0 50 50" style="top:16px" fill="none" stroke="#0c5a6e" stroke-width="4">
      <circle cx="25" cy="25" r="21"/>
      <circle cx="25" cy="25" r="12" stroke-width="3"/>
      <line x1="14" y1="36" x2="36" y2="14"/>
    </svg>
    <h2 style="top:78px">No Social<br>Security Number<br>Requires</h2>
  </div>

  <div class="benefit" style="left:1021px">
    <svg width="50" height="46" viewBox="0 0 50 46" style="top:16px" fill="none" stroke="#0c5a6e" stroke-width="2.5" stroke-linejoin="round" stroke-linecap="round">
      <line x1="25" y1="2" x2="25" y2="7"/><line x1="17" y1="4" x2="19" y2="9"/><line x1="33" y1="4" x2="31" y2="9"/>
      <path d="M3 22 L12 14 L20 22 L12 30 Z"/>
      <path d="M47 22 L38 14 L30 22 L38 30 Z"/>
      <path d="M16 26 L27 37 Q30 40 33 37 L36 32"/>
      <path d="M20 22 L28 16 L34 24"/>
      <path d="M22 32 L26 36"/>
    </svg>
    <h2 style="top:78px">No Impact on<br>your Credit<br>Score</h2>
  </div>
</div>
</body>
</html>
```